Wordpress Design Project - Australian Solar Company wants to start FRESH!

About us

Bright Meadow are a renewable energy company based in Perth Australia, but we also have offices all over Asia. We specialise in offering renewable energy solutions (Solar PV Systems and LED Lighting) to residential and commercial customers.

Our current website: www.brightmeadowenergy.com.au

Our needs

This will be a replacement website as we are not happy with our current layout. We have an Australian company doing our SEO and they have recommended a new layout which we wish to go with.

We really want a professional and easy to navigate website that will assist in bringing in more enquiries and phone calls.

Content

We have all the content and will get the design winner to add this after we have chosen the design we like.
It is important that the call to actions are presented well and are visible these are things like the free quote form and our phone number.

The layout as we have advised has been based on SEO research so we wish it to be exactly the same unless otherwise stated.

Call to action

Our main objective of the new website is for people to come to the home page and see us as a professional and reliable company to deal with and enquire further.

We really want as many people as we can to convert to a lead. We want every person that comes to the website to enquire online or call us. We feel it is important to have a contact us/quote form on every page of the website.

Functional requirements

We have a chatterbook and vidstream account so links to these would be needed

Design assets

The logo needs to be displayed as shown in the website layout brief

Colours – we would like fresh, subdued colours that are professional and appealing to the eye. We ask that you do not take the colours from the logo.

Current website dislikes – the things we currently dislike about our current website is that it is hard to find information and there is no clear call to action. The colours are really unappealing as well as it looks cheap not professional.
The graphics that we require for the slider on the home page will have to be given after the winner is chosen but we want there to be three sliders on rotation

- Credibility builder (employee infront of solar panel) that encourages we use all our own employees not subcontractors
- Residential Slider – picture of a couple and solar panel system with a testimonial
- Commercial slider – picture of commercial system with “find out how you can install solar for free* at your business”

Design ideas

The website needs to be mobile friendly as well
It is going to be a total rebuild from the current website as our current website really isn’t working for us.

Target Market(s)

Target Audience

Our target audience are both residential and commercial clients
Residential – we want to attract home owners that are interested in reducing their electricity bill and helping the environment. Generally these people are between the ages of 28-50+ both male and female.

Commercial – We want to appeal to key decision makers within the commercial sphere. For example – CEOs, Company Directors, Operation managers and business owners of any industry. These people will be interested in reducing their electricity bills and creating a clean green image for their business.
Our target audience will generally come to our website to get information and enquire for a quote/ product information.

Industry/Entity Type

Residential

Requirements
Must have
• MUST BE LAID OUT LIKE THIS:

http://www.docuvault.com/doc/849302715/Website-Layout

Must have Enquire Now forms on every page that read:

Name
Phone Number
How did you hear about us
Message

```html
<!DOCTYPE html>
<html lang="en">
<head>
<meta charset="utf-8">
<title>Bright Meadow — Home</title>
<link href="https://fonts.googleapis.com/css2?family=Roboto:ital,wght@0,300;0,400;0,700;1,400&family=Roboto+Condensed:wght@400;700&display=swap" rel="stylesheet">
<style>
:root{
  --green:#5a9e3a;
  --green-dark:#2f7d1e;
  --green-soft:#b5cf95;
  --green-text:#8dbd6a;
  --yellow:#ffd45a;
  --orange:#f39a1b;
  --ink:#2b2b2b;
  --body:#555;
  --footer:#333;
  --footer-field:#5e5e5e;
  --footer-text:#e2e2e2;
  --line:#cfcfcf;
}
*{box-sizing:border-box;margin:0;padding:0}
html,body{width:918px;height:1200px;overflow:hidden;background:#fff}
body{position:relative;font-family:'Roboto',sans-serif;color:var(--body)}
.abs{position:absolute}

/* header */
.brand{left:115px;top:22px;display:flex;align-items:center;gap:7px}
.brand-dot{width:30px;height:30px;border-radius:50%;background:var(--yellow)}
.brand-name{font-family:'Roboto Condensed',sans-serif;font-weight:700;font-size:21px;color:var(--green-dark)}
.phone{right:116px;top:14px;display:flex;align-items:center;gap:6px;font-family:'Roboto Condensed',sans-serif;font-size:19px;color:var(--yellow)}
.social-sq{display:inline-block;width:14px;height:14px;background:#3b5a99;border-radius:2px;margin-left:8px}
.nav{right:115px;top:55px;display:flex;gap:29px;font-family:'Roboto Condensed',sans-serif;font-weight:700;font-size:9.5px;color:var(--ink);letter-spacing:.2px}
.nav span::after{content:" ⌄";color:#888}
.nav span.plain::after{content:""}

/* hero */
.hero{left:0;top:86px;width:918px;height:286px;background:linear-gradient(160deg,#8ea8d8 0%,#3d5fae 35%,#2a4690 60%,#9fb1d6 80%,#6f6a5b 100%)}
.quote{left:588px;top:104px;width:214px;height:250px;background:var(--green-soft);border-radius:6px;padding:14px 10px}
.quote h2{font-family:'Roboto Condensed',sans-serif;font-weight:700;font-size:19px;color:var(--green-dark);text-align:center;margin-bottom:6px}
.field{background:#fff;height:25px;margin-bottom:4px;font-size:8px;font-style:italic;color:#666;padding:8px 7px}
.field.tall{height:66px}
.quote-btn{display:inline-block;margin-top:2px;background:var(--yellow);color:var(--orange);font-family:'Roboto Condensed',sans-serif;font-weight:700;font-size:13px;padding:6px 10px}

/* feature cards */
.card{top:415px;width:215px}
.card-img{height:125px;position:relative}
.card-title{position:absolute;left:0;bottom:0;width:100%;height:32px;background:rgba(50,50,50,.88);color:#fff;font-family:'Roboto Condensed',sans-serif;font-weight:700;font-size:12.5px;padding:9px 7px}
.card p{margin-top:12px;font-size:8.6px;line-height:14.4px;font-weight:300;color:#444}
.more{display:block;text-align:right;margin-top:4px;font-size:8px;font-style:italic;font-weight:700;color:var(--green-text);text-decoration:underline}

/* panels */
.panel{top:670px;height:250px;border:1px solid #d8d8d8;border-radius:5px;background:linear-gradient(#fff,#f2f2f2);padding:11px 14px}
.panel h3{font-family:'Roboto Condensed',sans-serif;font-weight:700;font-size:17.5px;color:var(--green-text);padding-bottom:4px;border-bottom:1px solid var(--line);margin-bottom:14px}
.welcome p{font-size:8.8px;line-height:14.4px;font-weight:300;color:#333}
.welcome-logo{float:right;width:122px;height:72px;border:1px solid #999;background:#fff;margin:0 0 4px 8px;display:flex;align-items:center;justify-content:center;gap:5px}
.welcome-logo .brand-dot{width:20px;height:20px}
.welcome-logo .brand-name{font-size:14px}
.video{height:185px;background:linear-gradient(90deg,#3a3127,#6b5a45 45%,#2a241d);position:relative}
.controls{position:absolute;left:0;bottom:0;width:100%;height:14px;background:#111;border-top:2px solid #444}
.controls i{position:absolute;left:0;top:-2px;width:18px;height:2px;background:#d22}

/* footer */
.footer{left:0;top:963px;width:918px;height:237px;background:var(--footer)}
.fcol{top:32px;width:156px}
.fcol h4{font-family:'Roboto Condensed',sans-serif;font-weight:700;font-size:11px;color:#bbb;padding-bottom:5px;border-bottom:1px solid #777;margin-bottom:12px}
.fcol li{list-style:none;font-size:7.7px;line-height:14.4px;color:var(--footer-text)}
.fcol li::before{content:"> "}
.fcol p{font-size:7.7px;line-height:14.4px;color:var(--footer-text)}
.ffield{background:var(--footer-field);height:21px;margin-bottom:4px;font-size:7.5px;font-style:italic;color:#ddd;padding:6px 7px}
.ffield.tall{height:64px}
.send{display:inline-block;margin-top:2px;background:var(--yellow);color:var(--orange);font-family:'Roboto Condensed',sans-serif;font-weight:700;font-size:11.5px;padding:5px 10px}
.icons{display:flex;gap:4px;margin-top:14px}
.icons span{width:14px;height:14px;border-radius:2px}
.copy{text-align:right;font-size:7px;font-style:italic;margin-top:14px;color:#ccc}
</style>
</head>
<body>

<header>
  <div class="abs brand"><span class="brand-dot"></span><span class="brand-name">Bright Meadow</span></div>
  <div class="abs phone">
    <svg width="24" height="18" viewBox="0 0 24 18"><path d="M3 6c0-4 18-4 18 0l-3 2-3-2H9L6 8z" fill="#c8872c"/><rect x="6" y="8" width="12" height="9" rx="2" fill="#e0a447"/><circle cx="12" cy="12.5" r="2.5" fill="#fff"/></svg>
    <span>(1300) 427 905</span><span class="social-sq" aria-label="chatterbook"></span>
  </div>
  <nav class="abs nav"><span>ABOUT US</span><span>PRODUCTS</span><span>SERVICES</span><span>WHY BRIGHT MEADOW</span><span class="plain">CONTACT</span></nav>
</header>

<section class="abs hero" role="img" aria-label="Rows of blue solar panels under a bright sky"></section>
<form class="abs quote">
  <h2>QUOTE ONLINE</h2>
  <div class="field">Name</div>
  <div class="field">Phone #</div>
  <div class="field">How did you hear about us</div>
  <div class="field tall">Message</div>
  <span class="quote-btn">Get a FREE Online Quote ›</span>
  <svg class="abs" style="left:184px;top:196px" width="34" height="38" viewBox="0 0 34 38"><path d="M28 2c6 14 0 26-14 27v7L2 24 14 12v8c9-1 14-8 14-18z" fill="#3f8a2a"/></svg>
</form>

<article class="abs card" style="left:115px">
  <div class="card-img" role="img" aria-label="Installer fitting solar panels on a house roof" style="background:linear-gradient(#8fb4dc,#35549a 60%,#27407a)"><div class="card-title">Perth Residential Solar Power</div></div>
  <p>Lorem ipsum dolor sit amet, consectetur adipiscing elit. Nullam lectus purus, placerat eget velit ac, molestie tincidunt lacus. Cras felis erat, scelerisque a erat ut, consectetur sodales ipsum. Nulla tincidu...</p>
  <span class="more">&gt; Read More</span>
</article>
<article class="abs card" style="left:352px">
  <div class="card-img" role="img" aria-label="Large commercial solar array on a flat roof" style="background:linear-gradient(#cfe3f2,#9fb08a 35%,#6f86a8 55%,#3c5690)"><div class="card-title">Perth Commercial Solar Power</div></div>
  <p>Pellentesque ut tincidunt tellus, ut dapibus risus. Fusce at egestas nulla, vel accumsan ligula. Aenean et dui mattis, varius elit ullamcorper, luctus tellus. Nulla hendrerit dignissim ligula. Curabitur...</p>
  <span class="more">&gt; Read More</span>
</article>
<article class="abs card" style="left:588px">
  <div class="card-img" role="img" aria-label="Close-up of an LED light bulb" style="background:radial-gradient(circle at 70% 40%,#d6ecff,#6e9fc4 45%,#2e5778)"><div class="card-title">Perth LED Lighting</div></div>
  <p>Aenean pharetra tortor a neque vulputate, elementum vehicula turpis molestie. Sed ornare purus lorem, nec lobortis sem dapibus faucibus. Proin posuere condimentum lectus eu pulvinar...</p>
  <span class="more">&gt; Read More</span>
</article>

<section class="abs panel welcome" style="left:115px;width:333px">
  <h3>WELCOME</h3>
  <div class="welcome-logo"><span class="brand-dot"></span><span class="brand-name">Bright Meadow</span></div>
  <p>Nunc feugiat fringilla elit. Vestibulum sit amet faucibus mauris. Aliquam erat volutpat. Integer cursus aliquet libero, ac scelerisque erat venenatis at. Vivamus nec nibh sit amet justo blandit dapibus. Vivamus semper metus non metus mattis, eget venenatis magna interdum. Class aptent taciti sociosqu ad litora torquent per conubia nostra, per inceptos himenaeos. Morbi blandit justo vitae mi ornare consequat. Etiam consectetur ipsum dui, non tincidunt dui sodales vitae. Class aptent taciti sociosqu ad litora torquent per conubia nostra, per inceptos himenaeos. Nullam gravida, nisl quis porttitor porta, orci urna pellentesque nisi, sed vestibulum mauris quam ut felis. Vivamus rutrum metus a fringilla euismod. Aliquam hendrerit congue ligula nec.</p>
</section>
<section class="abs panel" style="left:470px;width:333px">
  <h3>TESTIMONIALS</h3>
  <div class="video" role="img" aria-label="Video testimonial of a customer speaking in a living room"><div class="controls"><i></i></div></div>
</section>

<footer class="abs footer">
  <div class="abs fcol" style="left:115px">
    <h4>PRIMARY PROD. / SERVICES</h4>
    <ul><li>Perth LED Lighting</li><li>Solar Leasing</li><li>Air conditioning WA</li><li>Solar Systems</li><li>Electrical Systems</li><li>Refrigeration Systems</li></ul>
  </div>
  <div class="abs fcol" style="left:293px">
    <h4>MEMBERSHIPS</h4>
    <p>Lorem ipsum dolor sit amet, consectetur adipiscing elit. Ut adipiscing vulputatey ipsum euismod pharetra. Vivamus lorem libero, malesuada in arcu a, suscipit laoreet orci. Nullam justo purus, feugiat in porttitor ac, ultricies vitae ipsum. Integer in libero in neque lobortis elementum. Curabitur neque arcu, viverra at massa non, posuere suscipit magna cras pellentesque. luctus turpis sit amet scelerisque. Donec fermentum magna.</p>
  </div>
  <div class="abs fcol" style="left:470px">
    <h4>REQUEST A QUOTE</h4>
    <div class="ffield">Name</div>
    <div class="ffield">Email</div>
    <div class="ffield tall">Message</div>
    <span class="send">Send ›</span>
  </div>
  <div class="abs fcol" style="left:647px">
    <h4>BRIGHT MEADOW</h4>
    <p>U4 18 Kestrel Road<br>Willow Park, WA 6172<br><br>Phone: (08) 6391 2047<br>Fax: (08) 6391 2048<br>Email: sales@brightmeadowenergy.com.au</p>
    <div class="icons"><span style="background:#3b5a99" aria-label="chatterbook"></span><span style="background:#3fa9d6" aria-label="chirpline"></span><span style="background:#c4302b" aria-label="vidstream"></span><span style="background:#f08a24" aria-label="feed"></span><span style="background:#ddd" aria-label="email"></span></div>
    <p class="copy">©2013 Bright Meadow.</p>
  </div>
</footer>

</body>
</html>
```